Tressora hair oil bottle & packaging (Instagrammable)

I'm a blogger/social media influencer and I'm launching my own hair oil that I created myself. The hair oil is something I've used fora a long time and it makes your hair grow like there's no tomorrow!

I'm looking for a feminine and minimalistic bottle for the hair oil and also a nice packaging for the bottle. Please have a look at my Instagram account (@minabrellvik), I'd love if the product design and color scheme would be inspired by my Instagram feed. I'm looking for a design that would look very 'Instagrammable'

Product name: Tressora
Bottle size: 100ml

Thank you xx

Target Market(s)

Females

Requirements
Must have
• According to the law this has to be marked on the packaging and on the bottle:
• Amount: 100ml
• Marked on the packaging:
• Ingredients: Burdock root oil, Grapeseed oil, Organic castor oil (maybe somehow draw attention to the fact that it's organic when designing the bottle & packaging), peppermint oil, Lavender oil, Cedarwood oil, Rosemary oil
Nice to have
• I added some photos of Ki Wenna packaging - I absolutely love it! The colour is exactly what I have in mind (also if you check my Instagram it's kind of my 'feed colour' - I'd be happy if the packaging would look something like that. The Ki Wenna packaging is exactly what I meant by 'Instagrammable'.
• Also - if we go for something like this, we could write Glow up! on the inside (so you see that when opening the packaging) or feel free to come up with something yourself, just bear in mind it's a hair oil that promotes hair growth

```html
<!DOCTYPE html>
<html lang="en">
<head>
<meta charset="utf-8">
<title>Tressora – Organic Infused Hair Oil Label</title>
<link href="https://fonts.googleapis.com/css2?family=Josefin+Sans:wght@400;600&display=swap" rel="stylesheet">
<style>
  :root {
    --canvas-bg: #f1eff0;
    --label-blush: #f2e3df;
    --label-blush-light: #f6ece9;
    --wash-rose: #e6cfc9;
    --wash-grey: #dcd6d6;
    --ink: #2a2426;
    --ink-soft: #7a6c6c;
  }
  html, body {
    margin: 0;
    padding: 0;
    width: 1200px;
    height: 900px;
    overflow: hidden;
    background: var(--canvas-bg);
  }
  .canvas {
    position: relative;
    width: 1200px;
    height: 900px;
    background: var(--canvas-bg);
  }
  .bottle-label {
    position: absolute;
    left: 334px;
    top: 70px;
    width: 532px;
    height: 760px;
    background: linear-gradient(180deg, var(--label-blush) 0%, var(--label-blush-light) 100%);
    overflow: hidden;
  }
  .label-wash {
    position: absolute;
    left: 0;
    top: 270px;
    width: 532px;
    height: 270px;
    background:
      linear-gradient(172deg, transparent 0%, var(--wash-rose) 22%, transparent 40%),
      linear-gradient(176deg, transparent 35%, var(--wash-grey) 55%, transparent 75%),
      linear-gradient(170deg, transparent 60%, var(--wash-rose) 80%, transparent 100%);
    opacity: 0.85;
  }
  .brand-name {
    position: absolute;
    left: 0;
    width: 100%;
    top: 318px;
    margin: 0;
    text-align: center;
    font-family: "Josefin Sans", sans-serif;
    font-weight: 600;
    font-size: 92px;
    line-height: 1;
    letter-spacing: 2px;
    color: var(--ink);
    text-transform: lowercase;
  }
  .product-type {
    position: absolute;
    left: 0;
    width: 100%;
    top: 441px;
    margin: 0;
    text-align: center;
    font-family: "Josefin Sans", sans-serif;
    font-weight: 400;
    font-size: 19px;
    letter-spacing: 4px;
    color: var(--ink-soft);
    text-transform: uppercase;
  }
  .volume {
    position: absolute;
    left: 0;
    width: 100%;
    top: 632px;
    margin: 0;
    text-align: center;
    font-family: "Josefin Sans", sans-serif;
    font-weight: 400;
    font-size: 17px;
    letter-spacing: 0.5px;
    color: var(--ink);
  }
</style>
</head>
<body>
  <main class="canvas">
    <section class="bottle-label">
      <div class="label-wash" role="img" aria-label="Soft blush and grey watercolour brush-stroke wash across the label"></div>
      <h1 class="brand-name">Tressora</h1>
      <p class="product-type">Organic Infused Hair Oil</p>
      <p class="volume">100ml ℮ – 3.4 fl.oz.</p>
    </section>
  </main>
</body>
</html>
```